Bref créative
VELTRANO
VELTRANO Bar & Restaurant - Business Card/Stationary
I need double sided standard sized Business Card [3.5" x 2"]
Any legible font - but not boring!
Professional
Lucinda Marbella
chef de cuisine
K7 Harbor Plaza, GF/D
47th St.
Camp Valdoro
Taguig City, 1634
Manila, Philippines
veltranorestaurant@kestomail.example
facebook.example/veltranomanila, twitter.example/veltrano_

```html
<!DOCTYPE html>
<html lang="en">
<head>
<meta charset="utf-8">
<title>VELTRANO Bar &amp; Restaurant – Business Card</title>
<link rel="stylesheet" href="https://fonts.googleapis.com/css2?family=Open+Sans:ital,wght@0,400;0,700;1,400&family=Noto+Serif:wght@400;700&display=swap">
<style>
  :root {
    --backdrop: #d8d3cb;
    --card-dark: #1c1b1d;
    --card-light: #ffffff;
    --ink-light: #f2f2f2;
    --ink-muted: #cfcfcf;
    --ink-dark: #151515;
    --shadow: rgba(0, 0, 0, 0.28);
  }
  * { box-sizing: border-box; margin: 0; padding: 0; }
  html, body {
    width: 1200px;
    height: 852px;
    overflow: hidden;
    background: var(--backdrop);
  }
  .canvas {
    position: relative;
    width: 1200px;
    height: 852px;
  }
  .business-card {
    position: absolute;
    width: 580px;
    height: 332px;
    display: flex;
    border-radius: 22px;
    overflow: hidden;
    box-shadow: 0 10px 26px var(--shadow);
  }
  .business-card--first { left: 90px; top: 96px; }
  .business-card--second { left: 530px; top: 452px; }

  .card-info {
    width: 50%;
    background: var(--card-dark);
    color: var(--ink-light);
    padding: 46px 26px 30px 26px;
    display: flex;
    flex-direction: column;
  }
  .card-info--right { text-align: right; }

  .card-brand {
    width: 50%;
    background: var(--card-light);
    display: flex;
    align-items: center;
    justify-content: center;
  }
  .brand-name {
    font-family: "Noto Serif", serif;
    font-weight: 700;
    font-size: 30px;
    letter-spacing: 6px;
    color: var(--ink-dark);
  }

  .person-name {
    font-family: "Open Sans", sans-serif;
    font-weight: 700;
    font-size: 19px;
    line-height: 1.2;
  }
  .person-role {
    font-family: "Open Sans", sans-serif;
    font-size: 14px;
    color: var(--ink-muted);
    margin-top: 2px;
  }
  .address {
    font-family: "Noto Serif", serif;
    font-size: 13px;
    line-height: 1.45;
    margin-top: 40px;
    font-style: normal;
  }
  .contact-list {
    list-style: none;
    margin-top: auto;
    font-family: "Noto Serif", serif;
    font-size: 13px;
    line-height: 1.5;
  }
  .contact-row {
    display: flex;
    align-items: center;
    gap: 8px;
  }
  .card-info--right .contact-row { justify-content: flex-end; }
  .contact-icon {
    width: 14px;
    height: 14px;
    flex: none;
  }
  .contact-email { font-size: 12px; }
</style>
</head>
<body>
<main class="canvas">

  <article class="business-card business-card--first">
    <section class="card-info">
      <h1 class="person-name">Lucinda Marbella</h1>
      <p class="person-role">chef de cuisine</p>
      <address class="address">
        K7 Harbor Plaza, GF/D 47th St.<br>
        Camp Valdoro, Taguig City,<br>
        1634, Manila, Philippines
      </address>
      <ul class="contact-list">
        <li class="contact-row">
          <svg class="contact-icon" viewBox="0 0 14 14" aria-hidden="true"><rect x="3.5" y="1" width="7" height="12" rx="1.5" fill="none" stroke="currentColor" stroke-width="1.4"/><line x1="6" y1="11" x2="8" y2="11" stroke="currentColor" stroke-width="1.2"/></svg>
          <span>+63 2 555 0142<br>+63 917 555 0143</span>
        </li>
        <li class="contact-row contact-email">
          <svg class="contact-icon" viewBox="0 0 14 14" aria-hidden="true"><text x="7" y="11.5" text-anchor="middle" font-family="Open Sans, sans-serif" font-size="13" font-weight="700" fill="currentColor">@</text></svg>
          <span>veltranorestaurant@kestomail.example</span>
        </li>
      </ul>
    </section>
    <section class="card-brand">
      <span class="brand-name">VELTRANO</span>
    </section>
  </article>

  <article class="business-card business-card--second">
    <section class="card-brand">
      <span class="brand-name">VELTRANO</span>
    </section>
    <section class="card-info card-info--right">
      <h2 class="person-name">Lucinda Marbella</h2>
      <p class="person-role">chef de cuisine</p>
      <address class="address">
        K7 Harbor Plaza, GF/D 47th St.<br>
        Camp Valdoro, Taguig City,<br>
        1634, Manila, Philippines
      </address>
      <ul class="contact-list">
        <li class="contact-row">
          <span>+63 2 555 0142<br>+63 917 555 0143</span>
          <svg class="contact-icon" viewBox="0 0 14 14" aria-hidden="true"><rect x="3.5" y="1" width="7" height="12" rx="1.5" fill="none" stroke="currentColor" stroke-width="1.4"/><line x1="6" y1="11" x2="8" y2="11" stroke="currentColor" stroke-width="1.2"/></svg>
        </li>
        <li class="contact-row contact-email">
          <span>veltranorestaurant@kestomail.example</span>
          <svg class="contact-icon" viewBox="0 0 14 14" aria-hidden="true"><text x="7" y="11.5" text-anchor="middle" font-family="Open Sans, sans-serif" font-size="13" font-weight="700" fill="currentColor">@</text></svg>
        </li>
      </ul>
    </section>
  </article>

</main>
</body>
</html>
```